依頼詳細
依頼の詳細や参考URL等は添付の「依頼詳細.txt」に全てまとめましたので、そちらをご確認ください。
トップページのラフイメージは「toppage_image.jpg」を参照下さい。
サイトURL
ページ数
1ページ
希望イメージ
シンプル 複雑
単色 カラフル
暗い 明るい
日常 高級
遊び心 厳粛
未来的 伝統的
女性的 男性的
希望する色
背景色:アイボリー。差し色:薄紫色など淡い色で何色か使用。
納品ファイル
• イラストレーター形式 (.ai)
• フォトショップ形式 (.psd)
補足説明

レベルがみなさん高かったので非常に迷いましたが、水彩がうまくマッチしていて、ごあいさつや保育目標などの部分のデザインも気に入りましたのでこちらにしました。

今回はコンペに参加していただき、誠にありがとうございました。
みなさん素晴らしいデザインで迷いましたが、またコンペを依頼する際にはご提案していただけたら幸いです。

```html
<!DOCTYPE html>
<html lang="ja">
<head>
<meta charset="utf-8">
<title>ひだまりほいくえん</title>
<link href="https://fonts.googleapis.com/css2?family=Kosugi+Maru&family=M+PLUS+Rounded+1c:wght@400;700&display=swap" rel="stylesheet">
<style>
:root{
  --ivory:#fbf8ee;
  --ink:#6b5a4a;
  --soft-ink:#8d7f72;
  --lavender:#b7a3d8;
  --pink:#ef9fb6;
  --peach:#f3bf8a;
  --mint:#9fd3c0;
  --sky:#9cc8e6;
  --leaf:#a8c64a;
  --leaf-dark:#8aa83a;
  --band:#d9ecb8;
  --line:#e4dccd;
}
*{box-sizing:border-box;margin:0;padding:0}
html,body{width:1200px;height:3092px;overflow:hidden}
body{background:var(--ivory);font-family:"Kosugi Maru","M PLUS Rounded 1c",sans-serif;color:var(--ink);position:relative}
.page{position:relative;width:1200px;height:3092px}

/* header */
.site-header{position:absolute;top:0;left:0;width:1200px;height:220px}
.tagline{position:absolute;left:24px;top:14px;font-size:12px;color:var(--soft-ink)}
.brand{position:absolute;left:0;right:0;top:28px;text-align:center}
.brand-name{font-family:"M PLUS Rounded 1c",sans-serif;font-weight:700;font-size:40px;color:var(--ink);letter-spacing:4px;display:inline-flex;align-items:center;gap:12px}
.brand-name::before{content:"";width:18px;height:18px;border-radius:50%;background:var(--peach)}
.brand-sub{font-size:13px;color:var(--lavender);margin-top:4px;letter-spacing:2px}
.contact{position:absolute;right:40px;top:14px;font-size:15px;color:var(--ink);line-height:1.6}
.contact span{color:var(--lavender);font-size:12px;margin-right:6px}
.global-nav{position:absolute;left:170px;top:124px;width:860px;display:flex;justify-content:space-between;border-top:1px dashed var(--line);border-bottom:1px dashed var(--line);padding:12px 0}
.nav-item{width:140px;text-align:center;font-size:15px;color:var(--ink)}
.nav-item i{display:block;width:30px;height:30px;margin:0 auto 6px;border-radius:50%}

/* hero */
.hero{position:absolute;top:230px;left:0;width:1200px;height:410px}
.hero-side{position:absolute;top:20px;width:90px;height:370px;border-radius:14px;opacity:.55}
.hero-main{position:absolute;left:100px;top:0;width:1000px;height:410px;border-radius:20px;background:linear-gradient(135deg,#c9d9e8,#e8d9c8 45%,#d6c2a8);}
.hero-badge{position:absolute;right:120px;bottom:30px;width:110px;height:110px;border-radius:50%;background:var(--pink);color:#fff;font-size:15px;display:flex;align-items:center;justify-content:center;text-align:center;line-height:1.4}
.hero-dots{position:absolute;top:656px;left:0;width:1200px;display:flex;justify-content:center;gap:10px}
.hero-dots i{width:10px;height:10px;border-radius:50%;background:var(--line)}
.hero-dots i:first-child{background:var(--lavender)}

/* headings */
.section-title{font-family:"M PLUS Rounded 1c",sans-serif;font-weight:700;font-size:30px;color:var(--ink);text-align:center;letter-spacing:4px}
.section-title small{display:block;font-size:12px;color:var(--lavender);letter-spacing:2px;font-weight:400;margin-top:4px}

/* features */
.features{position:absolute;top:710px;left:0;width:1200px}
.features-lead{text-align:center;font-size:15px;line-height:2.1;margin-top:26px;color:var(--soft-ink)}
.features-lead b{color:var(--pink);font-size:20px;font-weight:400}
.feature-grid{position:absolute;top:200px;left:110px;width:980px;display:grid;grid-template-columns:repeat(4,230px);gap:20px}
.feature-card{height:230px;background:#fff;border:3px solid var(--c);border-radius:8px;padding:10px}
.feature-card .ph{height:150px;border-radius:4px;background:var(--bg)}
.feature-card p{font-size:12px;line-height:1.7;margin-top:8px;color:var(--soft-ink)}
.feature-wide{position:absolute;top:450px;left:110px;width:980px;display:grid;grid-template-columns:480px 480px;gap:20px}
.feature-wide .feature-card{height:220px;display:flex;gap:14px}
.feature-wide .ph{width:230px;height:196px;flex:none}
.feature-wide p{font-size:13px;margin-top:auto;margin-bottom:auto}

/* news */
.news{position:absolute;top:1430px;left:160px;width:880px;height:290px}
.news-head{display:flex;align-items:center;justify-content:space-between}
.news-title{font-family:"M PLUS Rounded 1c",sans-serif;font-weight:700;font-size:26px;padding:8px 28px;border:2px solid var(--line);border-radius:30px;background:#fff}
.news-bus{width:150px;height:70px;border-radius:16px;background:linear-gradient(#f6d46a,#f0b94a)}
.news-list{margin-top:20px;list-style:none}
.news-list li{display:flex;gap:40px;font-size:14px;padding:12px 10px;border-bottom:1px dashed var(--line);color:var(--soft-ink)}
.news-list time{color:var(--ink)}

/* banners */
.banner-band{position:absolute;top:1780px;left:0;width:1200px;height:180px;background:var(--band)}
.banner-row{position:absolute;top:20px;left:90px;width:1020px;display:flex;gap:30px}
.banner{width:320px;height:140px;border-radius:8px;display:flex;overflow:hidden;background:#fff}
.banner span{width:130px;display:flex;align-items:center;justify-content:center;text-align:center;color:#fff;font-size:16px;line-height:1.5;background:var(--c)}
.banner i{flex:1;background:var(--bg)}

/* greeting */
.greeting{position:absolute;top:2010px;left:0;width:1200px;height:470px}
.greeting-photo{position:absolute;left:90px;top:40px;width:380px;height:380px;border-radius:50%;background:radial-gradient(circle,#e8d6c4,#c9b9a2);border:8px solid #fff;box-shadow:0 0 0 3px var(--lavender)}
.greeting-bubble{position:absolute;left:70px;top:10px;width:120px;height:70px;border-radius:50%;background:#fff;border:2px solid var(--pink);font-size:13px;display:flex;align-items:center;justify-content:center;text-align:center;line-height:1.4}
.greeting-body{position:absolute;left:540px;top:80px;width:560px}
.greeting-body .section-title{text-align:left}
.greeting-body p{font-size:14px;line-height:2.1;margin-top:24px;color:var(--soft-ink)}

/* goals */
.goals{position:absolute;top:2480px;left:0;width:1200px;height:320px}
.goals .section-title{position:absolute;left:150px;top:10px;text-align:left}
.goal-list{position:absolute;left:150px;top:86px;list-style:none}
.goal-list li{display:flex;align-items:center;gap:16px;font-size:17px;margin-bottom:14px}
.goal-list b{width:42px;height:42px;border-radius:50%;display:flex;align-items:center;justify-content:center;color:#fff;background:var(--c);font-size:18px}
.goals-photo{position:absolute;right:140px;top:-20px;width:300px;height:300px;border-radius:50%;background:radial-gradient(circle,#dfe8c8,#b7c98e);border:8px solid #fff}
.goals-tree{position:absolute;right:40px;bottom:0;width:90px;height:160px;border-radius:45px 45px 10px 10px;background:linear-gradient(#c8dc7a,#a8c64a)}

/* footer */
.site-footer{position:absolute;top:2800px;left:0;width:1200px;height:292px;background:var(--leaf);color:#fff}
.footer-info{position:absolute;left:50px;top:36px;width:280px}
.footer-name{font-family:"M PLUS Rounded 1c",sans-serif;font-weight:700;font-size:26px;letter-spacing:1px;white-space:nowrap}
.footer-info p{font-size:13px;line-height:1.9;margin-top:14px}
.footer-map{position:absolute;left:370px;top:36px;width:300px;height:170px;background:#eef0e6;border-radius:4px}
.footer-links{position:absolute;left:740px;top:36px;display:grid;grid-template-columns:200px 200px;gap:4px 20px;list-style:none;font-size:13px;line-height:1.9}
.footer-links li::before{content:"› "}
.copyright{position:absolute;left:0;bottom:0;width:1200px;height:40px;background:var(--leaf-dark);font-size:11px;text-align:center;line-height:40px;letter-spacing:1px}
</style>
</head>
<body>
<div class="page">

<header class="site-header">
  <p class="tagline">みどり市の認可保育園 ひだまりほいくえん</p>
  <div class="brand">
    <div class="brand-name">ひだまりほいくえん</div>
    <div class="brand-sub">HIDAMARI HOIKUEN</div>
  </div>
  <div class="contact">
    <div><span>TEL</span>000-123-4567</div>
    <div><span>FAX</span>000-123-4568</div>
  </div>
  <nav class="global-nav">
    <a class="nav-item"><i style="background:var(--pink)"></i>園の案内</a>
    <a class="nav-item"><i style="background:var(--peach)"></i>保育の特色</a>
    <a class="nav-item"><i style="background:var(--mint)"></i>保育園の一日</a>
    <a class="nav-item"><i style="background:var(--sky)"></i>年間行事</a>
    <a class="nav-item"><i style="background:var(--lavender)"></i>送迎方法</a>
    <a class="nav-item"><i style="background:var(--leaf)"></i>緊急連絡網</a>
  </nav>
</header>

<section class="hero">
  <div class="hero-side" style="left:0;background:#d7c9b3"></div>
  <div class="hero-main" role="img" aria-label="園庭の遊具で遊ぶ子どもたちの写真"></div>
  <div class="hero-badge">入園のご案内</div>
  <div class="hero-side" style="right:0;background:#c9d6e2"></div>
</section>
<div class="hero-dots"><i></i><i></i><i></i></div>

<section class="features">
  <h2 class="section-title">園の特色<small>FEATURE</small></h2>
  <p class="features-lead">
    自然豊かな環境の中で、子どもたち一人ひとりの個性を大切にした保育を実践しています。<br>
    <b>延長</b>保育あり、<b>一時</b>保育あり、<b>休日</b>保育も実施<br>
    ご家庭と連携しながら、安心して過ごせる園づくりを進めています。
  </p>
  <div class="feature-grid">
    <div class="feature-card" style="--c:var(--sky);--bg:#d6e3ec"><div class="ph" role="img" aria-label="机で学ぶ子どもの写真"></div><p>年中から文字や数字の学習を取り入れています。</p></div>
    <div class="feature-card" style="--c:var(--lavender);--bg:#ece6f3"><div class="ph" role="img" aria-label="英語の教材の写真"></div><p>外国人講師による英語あそびを週に一度行います。</p></div>
    <div class="feature-card" style="--c:var(--mint);--bg:#e5dccb"><div class="ph" role="img" aria-label="園庭で遊ぶ子どもたちの写真"></div><p>広い園庭で思いきり体を動かして遊びます。</p></div>
    <div class="feature-card" style="--c:var(--peach);--bg:#f1e4d2"><div class="ph" role="img" aria-label="手作りの給食の写真"></div><p>園内の調理室で毎日手作りの給食を用意します。</p></div>
  </div>
  <div class="feature-wide">
    <div class="feature-card" style="--c:var(--pink);--bg:#e9d4c2"><div class="ph" role="img" aria-label="発表会で並ぶ子どもたちの写真"></div><p>季節の行事や発表会を通して、表現する喜びと友達と協力する大切さを学びます。</p></div>
    <div class="feature-card" style="--c:var(--leaf);--bg:#e6e1c8"><div class="ph" role="img" aria-label="給食を食べる子どもたちの写真"></div><p>食育にも力を入れ、野菜の栽培や収穫を体験しながら食べる楽しさを育てます。</p></div>
  </div>
</section>

<section class="news">
  <div class="news-head">
    <h2 class="news-title">新着情報</h2>
    <div class="news-bus" role="img" aria-label="送迎バスのイラスト"></div>
  </div>
  <ul class="news-list">
    <li><time>2015.00.00</time>運動会のお知らせを掲載しました。</li>
    <li><time>2015.00.00</time>来年度の入園説明会の日程が決まりました。</li>
    <li><time>2015.00.00</time>園だよりを更新しました。</li>
    <li><time>2015.00.00</time>夏まつりの写真を掲載しました。</li>
    <li><time>2015.00.00</time>ホームページを公開しました。</li>
  </ul>
</section>

<section class="banner-band">
  <div class="banner-row">
    <a class="banner" style="--c:var(--leaf);--bg:#e5d8c4"><span>入園の<br>ご案内</span><i role="img" aria-label="子どもの写真"></i></a>
    <a class="banner" style="--c:var(--pink);--bg:#dfd2c0"><span>先生の<br>紹介</span><i role="img" aria-label="先生と子どもの写真"></i></a>
    <a class="banner" style="--c:var(--sky);--bg:#d9d2c6"><span>先生の<br>行事予定表</span><i role="img" aria-label="行事の写真"></i></a>
  </div>
</section>

<section class="greeting">
  <div class="greeting-photo" role="img" aria-label="遊ぶ子どもたちの写真"></div>
  <div class="greeting-bubble">いっしょに<br>あそぼう！</div>
  <div class="greeting-body">
    <h2 class="section-title">ご挨拶<small>GREETING</small></h2>
    <p>当園では、子どもたちが毎日笑顔で過ごせるよう、家庭的で温かな雰囲気づくりを大切にしています。<br>
    保護者の皆さまと手を取り合い、一人ひとりの成長をゆっくりと見守りながら、心と体の豊かな発達を支えてまいります。<br>
    また、地域とのつながりを大切にし、さまざまな体験を通して生きる力を育む保育を目指しています。どうぞお気軽にお越しください。</p>
  </div>
</section>

<section class="goals">
  <h2 class="section-title">保育目標<small>GOAL</small></h2>
  <ul class="goal-list">
    <li><b style="--c:var(--pink)">1</b>心身ともにたくましく遊ぶこども</li>
    <li><b style="--c:var(--peach)">2</b>身近な人を思いやり優しく接するこども</li>
    <li><b style="--c:var(--sky)">3</b>生命の素晴らしさを感じ心豊かなこども</li>
    <li><b style="--c:var(--lavender)">4</b>創意工夫し最後までやり遂げるこども</li>
  </ul>
  <div class="goals-photo" role="img" aria-label="運動会で走る子どもの写真"></div>
  <div class="goals-tree" role="img" aria-label="木のイラスト"></div>
</section>

<footer class="site-footer">
  <div class="footer-info">
    <div class="footer-name">ひだまりほいくえん</div>
    <p>社会福祉法人 ひだまり会<br>〒000-0000<br>みどり市さくら町1丁目2-3<br>TEL 000-123-4567</p>
  </div>
  <div class="footer-map" role="img" aria-label="園周辺の地図"></div>
  <ul class="footer-links">
    <li>トップ</li><li>入園案内</li>
    <li>園の案内</li><li>先生の紹介</li>
    <li>保育の特色</li><li>行事予定表</li>
    <li>保育園の一日</li><li>お問い合わせ</li>
    <li>年間行事</li><li>個人情報保護方針</li>
  </ul>
  <div class="copyright">COPYRIGHT © HIDAMARI HOIKUEN ALL RIGHTS RESERVED.</div>
</footer>

</div>
</body>
</html>
```